Simple proffessional BC

I have a logo which I will attach below.
I would like the logo on the front of the card with these details in point form below:
Pre and Post Natal Yoga: Pregnancy Workshops: Hypnobirthing Courses
On the back of the card my details:
Merrin Galvey
Facebook page- calmbellieswillowharbour
Mobile- 0438 512 740

I like the idea of the card being simple, possibly just the above on a plain coloured (eggshell?) card, a card that is textured.
I am open to suggestion if it appeals!
Thank you and good luck!

Target Market(s)

Pregnant women, 20's-40's

Requirements
Must have
• Simple, compliment logo.
Make logo the feature.
Should not have

• .

```html
<!DOCTYPE html>
<html lang="en">
<head>
<meta charset="utf-8">
<title>Calm Bellies – Business Card</title>
<link rel="stylesheet" href="https://fonts.googleapis.com/css2?family=Raleway:wght@300;400&display=swap">
<style>
  :root {
    --maroon: #7c1517;
    --orange: #eca53c;
    --accent-fill: #b45a2a;
    --white: #ffffff;
    --page: #ffffff;
  }
  html, body {
    margin: 0;
    padding: 0;
    width: 928px;
    height: 1200px;
    overflow: hidden;
    background: var(--page);
    font-family: "Raleway", sans-serif;
  }
  .canvas {
    position: relative;
    width: 928px;
    height: 1200px;
  }
  .card {
    position: absolute;
    left: 186px;
    width: 510px;
    height: 290px;
    border-radius: 16px;
    overflow: hidden;
  }
  /* Front */
  .card-front {
    top: 224px;
    background: var(--white);
  }
  .front-topband {
    position: absolute;
    left: 0; top: 0;
    width: 100%;
    height: 22px;
    background: var(--maroon);
  }
  .brand {
    position: absolute;
    left: 18px;
    top: 50px;
    display: flex;
    align-items: center;
    gap: 12px;
  }
  .brand-mark {
    width: 70px;
    height: 70px;
    border-radius: 50%;
    background: var(--orange);
  }
  .brand-name {
    font-weight: 400;
    font-size: 40px;
    color: var(--maroon);
  }
  .front-services {
    position: absolute;
    left: 0;
    top: 146px;
    width: 100%;
    height: 144px;
    background: var(--maroon);
  }
  .service-list {
    list-style: none;
    margin: 0;
    padding: 0;
    position: absolute;
    left: 18px;
    top: 36px;
  }
  .service-list li {
    position: relative;
    padding-left: 18px;
    height: 30px;
    line-height: 30px;
    font-size: 17px;
    font-weight: 300;
    color: var(--white);
  }
  .service-list li::before {
    content: "";
    position: absolute;
    left: 0;
    top: 11px;
    width: 8px;
    height: 8px;
    border-radius: 50%;
    background: var(--orange);
  }
  .accent-area {
    position: absolute;
    right: 6px;
    top: 36px;
    width: 52px;
    height: 100px;
    border-radius: 26px;
    background: var(--accent-fill);
  }
  /* Back */
  .card-back {
    top: 639px;
    background: var(--orange);
  }
  .contact-band {
    position: absolute;
    left: 0;
    top: 153px;
    width: 100%;
    height: 96px;
    background: var(--maroon);
    color: var(--white);
    font-weight: 300;
  }
  .contact-name {
    position: absolute;
    left: 40px;
    top: 8px;
    margin: 0;
    font-size: 20px;
    font-weight: 300;
  }
  .contact-line {
    position: absolute;
    left: 18px;
    display: flex;
    align-items: center;
    gap: 8px;
  }
  .contact-phone { top: 38px; font-size: 19px; }
  .contact-social { top: 66px; font-size: 14px; }
  .icon { width: 14px; height: 18px; display: block; }
  .social-square {
    width: 14px;
    height: 14px;
    border-radius: 2px;
    background: var(--white);
  }
</style>
</head>
<body>
<main class="canvas">
  <section class="card card-front" aria-label="Card front">
    <div class="front-topband"></div>
    <div class="brand">
      <div class="brand-mark"></div>
      <span class="brand-name">Calm Bellies</span>
    </div>
    <div class="front-services">
      <ul class="service-list">
        <li>Pre and post Natal yoga</li>
        <li>Pregnancy workshops</li>
        <li>Hypnobirthing courses</li>
      </ul>
      <div class="accent-area" role="img" aria-label="Decorative cluster of orange dots"></div>
    </div>
  </section>

  <section class="card card-back" aria-label="Card back">
    <div class="contact-band">
      <p class="contact-name">Merrin Galvey</p>
      <div class="contact-line contact-phone">
        <svg class="icon" viewBox="0 0 14 18" aria-hidden="true">
          <rect x="2" y="1" width="10" height="16" rx="2" fill="#ffffff"/>
          <rect x="4" y="3.5" width="6" height="6" fill="#7c1517"/>
          <circle cx="7" cy="13.5" r="1.3" fill="#7c1517"/>
        </svg>
        <span>0438 512 740</span>
      </div>
      <div class="contact-line contact-social">
        <span class="social-square"></span>
        <span>calmbellieswillowharbour</span>
      </div>
    </div>
  </section>
</main>
</body>
</html>
```